Consultancy Business Card Design

We need a business card design for a new company based in singapore called FortyOne. FortyOne a boutique consultancy firm offering broad-based business solutions, from conception to re-invention, for ventures from new start-ups to long-running traditional businesses.
Its 2 main divisions (Food & Beverage Operations and Construction & Project Management) have access to a wide range of networks, knowledge bases, and resources to service its clients across numerous diverse sectors. This includes, and is not limited to, construction, F&B, and retail.
We are a company that combines the ambition, boldness and energy of one in the 20s with the dedication, level-headedness and dependability of one entering its 30s. Bridging the experiences of the old with ideals of the young, we draw on the positives of both to create a unique synergy.
We hope to see designs that fits our company profile.
Boutique
FortyOne(Company Name)
Marcus Leow (Name)
Principle Consultant (Title)
F&B and Hospitality (Division)
(+65) 8364 5170 (Contact no.)
marcus@fortyone-example.com.sg (Email)

```html
<!DOCTYPE html>
<html lang="en">
<head>
<meta charset="utf-8">
<title>FortyOne Business Card</title>
<link rel="stylesheet" href="https://fonts.googleapis.com/css2?family=Arimo:wght@400;700&family=Marcellus&display=swap">
<style>
  :root {
    --page-bg: #d9d9db;
    --card-dark: #3f3f42;
    --card-dark-edge: #2e2e30;
    --green-deep: #2f5a17;
    --green-mid: #4e7f2a;
    --green-light: #93b95f;
    --logo-green: #a6d15f;
    --text-white: #ffffff;
    --shadow: rgba(0, 0, 0, 0.28);
  }
  html, body {
    margin: 0;
    width: 1200px;
    height: 900px;
    overflow: hidden;
    background: var(--page-bg);
  }
  .sheet {
    width: 1200px;
    height: 900px;
    display: flex;
    flex-direction: column;
    align-items: center;
    justify-content: center;
    gap: 40px;
  }
  .card {
    position: relative;
    width: 700px;
    height: 400px;
    box-shadow: 0 10px 24px var(--shadow);
    overflow: hidden;
  }
  .card-front {
    background: linear-gradient(135deg, var(--card-dark-edge) 0%, var(--card-dark) 50%, #4a4a4d 100%);
    display: flex;
    align-items: center;
    justify-content: center;
  }
  .wordmark {
    font-family: "Arimo", sans-serif;
    font-weight: 700;
    color: var(--logo-green);
    letter-spacing: -0.02em;
    margin: 0;
    line-height: 1;
  }
  .card-front .wordmark { font-size: 120px; }
  .card-back {
    background:
      radial-gradient(ellipse 78% 82% at 50% 100%, var(--green-light) 0%, var(--green-mid) 45%, var(--green-deep) 82%, transparent 83%),
      linear-gradient(180deg, var(--card-dark-edge) 0%, var(--card-dark) 100%);
  }
  .identity {
    position: absolute;
    left: 48px;
    top: 70px;
    color: var(--text-white);
    font-family: "Marcellus", serif;
  }
  .identity .person-name {
    margin: 0 0 10px;
    font-size: 38px;
    font-weight: 400;
    line-height: 1;
  }
  .identity .person-role {
    margin: 0;
    font-size: 21px;
    line-height: 1.15;
  }
  .card-back .wordmark {
    position: absolute;
    right: 60px;
    top: 185px;
    font-size: 72px;
  }
  .contacts {
    position: absolute;
    left: 48px;
    right: 40px;
    bottom: 48px;
    display: flex;
    justify-content: space-between;
    font-family: "Arimo", sans-serif;
    font-size: 22px;
    color: var(--text-white);
  }
  .contact-item {
    display: flex;
    align-items: center;
    gap: 10px;
  }
  .contact-item svg { flex: none; }
</style>
</head>
<body>
<main class="sheet">
  <section class="card card-front" aria-label="Card front">
    <p class="wordmark">FortyOne</p>
  </section>

  <section class="card card-back" aria-label="Card back">
    <div class="identity">
      <h1 class="person-name">Marcus Leow</h1>
      <p class="person-role">Principle Consultant</p>
      <p class="person-role">F&amp;B and Hospitality</p>
    </div>
    <p class="wordmark">FortyOne</p>
    <div class="contacts">
      <span class="contact-item">
        <svg width="20" height="20" viewBox="0 0 24 24" aria-hidden="true">
          <path fill="#ffffff" d="M6.6 10.8c1.4 2.8 3.8 5.1 6.6 6.6l2.2-2.2c.3-.3.7-.4 1-.2 1.1.4 2.3.6 3.6.6.6 0 1 .4 1 1V20c0 .6-.4 1-1 1C10.6 21 3 13.4 3 4c0-.6.4-1 1-1h3.5c.6 0 1 .4 1 1 0 1.3.2 2.5.6 3.6.1.3 0 .7-.2 1l-2.3 2.2z"/>
        </svg>
        (+65) 8364 5170
      </span>
      <span class="contact-item">
        <svg width="30" height="20" viewBox="0 0 30 20" aria-hidden="true">
          <rect x="0" y="0" width="30" height="20" rx="1.5" fill="#ffffff"/>
          <path d="M1 1 L15 12 L29 1" fill="none" stroke="#4e7f2a" stroke-width="2"/>
        </svg>
        marcus@fortyone-example.com.sg
      </span>
    </div>
  </section>
</main>
</body>
</html>
```